Design a Travel and Tourism website

We would like a freelancer to design a website that is essentially easy to use and navigate database providing local information for Travelers about destination countries.

We proposed website would discuss different rates, fees, visa requirement, resort locations, cheap flights, etc. This website should be elegant and modern. Our business name is mirdalon.
Some reference websites are plendavix.ca, gosthandiverquo.com,
There should be a forum in the website where travell\ers discuss about their first hand tranvel experience to such destinations.

```html
<!DOCTYPE html>
<html lang="en">
<head>
<meta charset="utf-8">
<title>mirdalon — travel story</title>
<link href="https://fonts.googleapis.com/css2?family=Mulish:wght@300;400;600;700;800&display=swap" rel="stylesheet">
<style>
  :root {
    --ink: #4a5366;
    --ink-soft: #5b6680;
    --muted: #a3a8b2;
    --line: #c9ccd3;
    --page: #ffffff;
    --screen: #ffffff;
    --sky: #e7e9e0;
    --field: #9c6a3a;
  }
  * { margin: 0; padding: 0; box-sizing: border-box; }
  html, body { width: 1200px; height: 1200px; overflow: hidden; background: var(--page); }
  body { font-family: "Mulish", sans-serif; color: var(--ink); position: relative; }

  .brand {
    position: absolute; left: 80px; top: 66px;
    display: flex; align-items: center; gap: 18px;
  }
  .brand-dot { width: 46px; height: 46px; border-radius: 50%; border: 4px solid var(--ink); }
  .brand-name { font-size: 44px; font-weight: 300; letter-spacing: 1px; color: var(--ink); text-transform: uppercase; }

  .screen {
    position: absolute; left: 305px; top: 150px;
    width: 590px; height: 1030px;
    background: var(--screen);
    box-shadow: 0 0 0 1px #eceef1;
    overflow: hidden;
  }

  .topbar { position: relative; height: 155px; }
  .topbar-brand {
    position: absolute; left: 44px; top: 70px;
    display: flex; align-items: center; gap: 8px;
  }
  .topbar-dot { width: 18px; height: 18px; border-radius: 50%; border: 3px solid var(--ink); }
  .topbar-name { font-size: 20px; font-weight: 700; color: var(--ink); }
  .lang {
    position: absolute; left: 190px; top: 74px;
    font-size: 17px; font-weight: 700; color: var(--ink);
    display: flex; align-items: center; gap: 6px;
  }
  .menu-toggle { position: absolute; left: 474px; top: 77px; width: 60px; }
  .menu-toggle span { display: block; height: 2px; background: var(--ink); margin-bottom: 15px; }

  .hero {
    position: absolute; left: 0; top: 155px; width: 590px; height: 437px;
    background: linear-gradient(180deg, #e6e8df 0%, #dfe1d9 18%, #8f96a0 30%, #4a4a4c 42%, #8a6a48 50%, #a8723f 70%, #8a5a30 100%);
  }

  .author-photo {
    position: absolute; left: 237px; top: 537px;
    width: 118px; height: 118px; border-radius: 50%;
    border: 5px solid #eef0f2;
    background: radial-gradient(circle at 50% 45%, #e8c1a4 0%, #c98f62 55%, #7a4a2a 100%);
  }

  .post-meta { position: absolute; left: 0; top: 662px; width: 590px; text-align: center; }
  .author { font-size: 22px; font-weight: 700; color: var(--ink-soft); }
  .posted { font-size: 18px; font-weight: 400; color: var(--ink-soft); margin-top: 2px; }
  .place {
    margin-top: 20px; font-size: 18px; font-weight: 300;
    letter-spacing: 3px; color: var(--muted); text-transform: uppercase;
  }

  .excerpt {
    position: absolute; left: 120px; top: 782px; width: 350px;
    font-size: 20px; line-height: 27px; font-weight: 400;
    text-align: center; color: var(--ink-soft);
  }
  .nav-arrow { position: absolute; top: 803px; }
  .nav-arrow.prev { left: 48px; }
  .nav-arrow.next { left: 512px; }

  .comment-button {
    position: absolute; left: 160px; top: 933px; width: 292px; height: 54px;
    border: 1.5px solid var(--ink); border-radius: 10px;
    display: flex; align-items: center; justify-content: center;
    font-family: "Mulish", sans-serif; font-size: 22px; font-weight: 700;
    color: var(--ink); background: transparent;
  }
</style>
</head>
<body>
  <header class="brand">
    <span class="brand-dot"></span>
    <span class="brand-name">mirdalon</span>
  </header>

  <main class="screen">
    <div class="topbar">
      <div class="topbar-brand">
        <span class="topbar-dot"></span>
        <span class="topbar-name">mirdalon</span>
      </div>
      <div class="lang">FR
        <svg width="18" height="12" viewBox="0 0 18 12"><polyline points="2,2 9,9 16,2" fill="none" stroke="#4a5366" stroke-width="2.2"/></svg>
      </div>
      <div class="menu-toggle" aria-label="Menu"><span></span><span></span><span></span></div>
    </div>

    <div class="hero" role="img" aria-label="Hiker with a backpack walking through golden grassland toward snow-capped mountains"></div>
    <div class="author-photo" role="img" aria-label="Profile photo of the author"></div>

    <section class="post-meta">
      <p class="author">by janedoe</p>
      <p class="posted">posted 5 days ago</p>
      <p class="place">Scotland</p>
    </section>

    <svg class="nav-arrow prev" width="32" height="58" viewBox="0 0 32 58"><polyline points="30,1 2,29 30,57" fill="none" stroke="#c9ccd3" stroke-width="1.5"/></svg>
    <p class="excerpt">Lorem ipsum dolor sit amet, consectetur adipisicing elit, sed do eiusmod tempor incididunt ut labore et dolore magna aliqua.</p>
    <svg class="nav-arrow next" width="32" height="58" viewBox="0 0 32 58"><polyline points="2,1 30,29 2,57" fill="none" stroke="#c9ccd3" stroke-width="1.5"/></svg>

    <div class="comment-button">comment</div>
  </main>
</body>
</html>
```